Flyer Designer for a Widow and Door Company - loooking for fresh design

We are looking for a flyer designed to advertise our business - we supply and install windows and doors - we are looking for a fresh looking flyer to distribute to drum up business - more information can be found at our website www.brightpanehouse.co.uk - We want a different approach than we currently have - making it vibrant and fresh - you can see the services on the website but its more the graphical design that we are looking for rather than content as the content from the website can be used for each service etc.

Target Market(s)

the general public

Colors

Designer to choose colors to be used in the design.

Requirements
Must have
• vibrant design and images

```html
<!DOCTYPE html>
<html lang="en">
<head>
<meta charset="utf-8">
<title>Bright Pane House – Flyer</title>
<link href="https://fonts.googleapis.com/css2?family=Ubuntu:wght@400;500;700&display=swap" rel="stylesheet">
<style>
  :root {
    --blue: #2b71b8;
    --blue-light: #4c9bd8;
    --grey-dark: #58595b;
    --grey-mid: #8a8c8f;
    --ink: #1e1e1e;
    --paper: #ffffff;
    --ring: #d9dadc;
  }
  * { margin: 0; padding: 0; box-sizing: border-box; }
  html, body { width: 960px; height: 1200px; overflow: hidden; background: var(--paper); }
  body { font-family: "Ubuntu", sans-serif; color: var(--ink); position: relative; }

  .hero {
    position: absolute; left: 0; top: 0; width: 960px; height: 450px;
    background: linear-gradient(100deg, #a4553d 0%, #c98a6e 35%, #e9e2da 60%, #b9c5d3 80%, #4f6d8e 100%);
  }
  .hero-wave { position: absolute; left: 0; top: 390px; width: 960px; height: 90px; }

  .brand { position: absolute; left: 40px; top: 485px; display: flex; align-items: center; gap: 16px; }
  .brand-mark { width: 74px; height: 74px; background: var(--blue); }
  .brand-name { font-weight: 700; font-size: 34px; line-height: 1.05; color: var(--blue); letter-spacing: 0.5px; }
  .brand-tagline { position: absolute; left: 130px; top: 570px; font-weight: 500; font-size: 15px; letter-spacing: 1.5px; color: var(--blue); }

  .intro { position: absolute; left: 40px; top: 612px; width: 442px; font-size: 15.5px; line-height: 22px; text-align: justify; }
  .intro p + p { margin-top: 22px; }

  .gallery { position: absolute; left: 503px; top: 470px; display: grid; grid-template-columns: 205px 205px; gap: 16px; }
  .gallery .tile { height: 150px; border: 3px solid #fff; box-shadow: 0 2px 6px rgba(0,0,0,0.25); }
  .tile-house { background: linear-gradient(160deg, #dfe5ea, #c9a27a 60%, #6d7a4e); }
  .tile-door { background: linear-gradient(90deg, #3e4a55, #eef0f1 35%, #f6f6f4 65%, #4b5660); }
  .tile-bay { background: linear-gradient(170deg, #c8d4de, #a3533c 55%, #5b6d3f); }
  .tile-home { background: linear-gradient(165deg, #bcd3e6, #e8ddcc 45%, #a24b33 80%, #6f7f4b); }

  .service { position: absolute; width: 330px; }
  .service-icon { position: absolute; left: -76px; top: 0; width: 64px; height: 64px; }
  .service-title { font-weight: 400; font-size: 21px; color: var(--blue); padding-bottom: 4px; border-bottom: 1px solid var(--grey-mid); width: 163px; white-space: nowrap; }
  .service-text { margin-top: 8px; font-size: 14.5px; line-height: 18.5px; color: #333; text-align: justify; }
  .svc-windows { left: 145px; top: 796px; }
  .svc-doors { left: 145px; top: 918px; }
  .svc-repairs { left: 604px; top: 796px; }
  .svc-landlord { left: 604px; top: 918px; }

  .footer-shape { position: absolute; left: 0; top: 1020px; width: 960px; height: 180px; }
  .cta { position: absolute; left: 40px; top: 1112px; font-size: 26px; color: var(--blue-light); }
  .contacts { position: absolute; left: 38px; top: 1156px; display: flex; gap: 22px; align-items: center; color: #fff; font-size: 20px; font-weight: 500; }
  .contact { display: flex; align-items: center; gap: 8px; }
  .contact svg { width: 20px; height: 20px; }
</style>
</head>
<body>

<div class="hero" role="img" aria-label="Photograph of a red-brick detached house with white sash windows and a smiling family of four standing in front"></div>
<svg class="hero-wave" viewBox="0 0 960 90" preserveAspectRatio="none">
  <path d="M0 90 L0 52 C250 2 520 10 720 40 C820 55 900 40 960 18 L960 90 Z" fill="#ffffff"/>
  <path d="M0 52 C250 2 520 10 720 40 C820 55 900 40 960 18 L960 30 C900 55 820 70 720 56 C520 26 250 18 0 66 Z" fill="var(--blue)"/>
</svg>

<div class="brand">
  <div class="brand-mark"></div>
  <div class="brand-name">BRIGHT PANE<br>HOUSE LTD</div>
</div>
<div class="brand-tagline">BESPOKE WINDOWS &amp; DOORS</div>

<div class="intro">
  <p>Bright Pane House are Suppliers and installers of quality windows and doors across Northamptonshire and surrounding villages.</p>
  <p>Offering a friendly, customer focused approach to your replacement windows and doors . Providing a full colour range of uPVc and aluminium to compliment any home.</p>
</div>

<div class="gallery">
  <div class="tile tile-house" role="img" aria-label="Photo of a cream house with oak-effect windows and a porch"></div>
  <div class="tile tile-door" role="img" aria-label="Photo of a white panelled front door between columns"></div>
  <div class="tile tile-bay" role="img" aria-label="Photo of a white bay window on a brick house"></div>
  <div class="tile tile-home" role="img" aria-label="Photo of a rendered brick home with wood-effect windows and door"></div>
</div>

<div class="service svc-windows">
  <svg class="service-icon" viewBox="0 0 64 64"><circle cx="32" cy="32" r="30" fill="#fff" stroke="var(--ring)" stroke-width="3"/><rect x="19" y="17" width="26" height="30" fill="none" stroke="var(--blue)" stroke-width="3"/><line x1="32" y1="17" x2="32" y2="47" stroke="var(--blue)" stroke-width="3"/><rect x="22" y="21" width="7" height="22" fill="none" stroke="var(--blue)" stroke-width="2"/></svg>
  <div class="service-title">Our Windows</div>
  <p class="service-text">Our windows are individually designed to suit your home. Our windows offer an exceptional level of energy efficency with market leading locking systems.</p>
</div>

<div class="service svc-doors">
  <svg class="service-icon" viewBox="0 0 64 64"><circle cx="32" cy="32" r="30" fill="#fff" stroke="var(--ring)" stroke-width="3"/><rect x="21" y="14" width="22" height="36" fill="var(--blue)"/><rect x="24" y="18" width="6" height="12" fill="#fff"/><rect x="34" y="18" width="6" height="12" fill="#fff"/><circle cx="38" cy="36" r="1.5" fill="#fff"/></svg>
  <div class="service-title">Our Doors</div>
  <p class="service-text">A new door from Bright Pane House can transform the look of your home, offer increased thermal efficiency and dramatically improve security for your peace of mind.</p>
</div>

<div class="service svc-repairs">
  <svg class="service-icon" viewBox="0 0 64 64"><circle cx="32" cy="32" r="30" fill="#fff" stroke="var(--ring)" stroke-width="3"/><path d="M22 44 L38 28 M36 22 a7 7 0 1 0 8 8 l-4 -1 -3 -3 z" stroke="var(--blue)" stroke-width="4" fill="none" stroke-linecap="round"/></svg>
  <div class="service-title">Repairs</div>
  <p class="service-text">At Bright Pane House we offer a full repair and replacement service on glass units, windows and doors. No job is too small.</p>
</div>

<div class="service svc-landlord">
  <svg class="service-icon" viewBox="0 0 64 64"><circle cx="32" cy="32" r="30" fill="#fff" stroke="var(--ring)" stroke-width="3"/><circle cx="29" cy="29" r="10" fill="none" stroke="var(--blue)" stroke-width="4"/><line x1="36" y1="36" x2="46" y2="46" stroke="var(--blue)" stroke-width="5" stroke-linecap="round"/></svg>
  <div class="service-title">Landlord Services</div>
  <p class="service-text">We work closely with Landlords &amp; Letting Agents to offer a full repair or replacement service on glass units, windows and doors as well as adjustments and replacement or repair of hinges, handles locks and cylinders.</p>
</div>

<svg class="footer-shape" viewBox="0 0 960 180" preserveAspectRatio="none">
  <path d="M0 30 C300 70 600 98 960 100 L960 180 L0 180 Z" fill="var(--grey-dark)"/>
</svg>
<div class="cta">Call today for your FREE QUOTE</div>
<div class="contacts">
  <span class="contact"><svg viewBox="0 0 20 20"><circle cx="10" cy="10" r="9" fill="none" stroke="var(--blue-light)" stroke-width="1.5"/><rect x="5" y="7" width="10" height="7" fill="var(--blue-light)"/></svg>sales@brightpanehouse.co.uk</span>
  <span class="contact"><svg viewBox="0 0 20 20"><circle cx="10" cy="10" r="9" fill="none" stroke="var(--blue-light)" stroke-width="1.5"/><path d="M7 5 l2 3 -1.5 1.5 a6 6 0 0 0 3 3 L12 11 l3 2 -1.5 2 C9 15 5 11 5 6.5 Z" fill="var(--blue-light)"/></svg>01632 960418</span>
  <span class="contact"><svg viewBox="0 0 20 20"><circle cx="10" cy="10" r="8" fill="none" stroke="var(--blue-light)" stroke-width="1.5"/><ellipse cx="10" cy="10" rx="3.5" ry="8" fill="none" stroke="var(--blue-light)" stroke-width="1.2"/><line x1="2" y1="10" x2="18" y2="10" stroke="var(--blue-light)" stroke-width="1.2"/></svg>brightpanehouse.co.uk</span>
</div>

</body>
</html>
```